Past the Gravel

I need a book cover designed - 6 inches wide x 9 inches tall. I would like it Past the predominantly black and white, with a big bold title as attached:
Past the
GRAVEL
I have attached a black and white photo that I would like to cover the bottom half (or close to it) of the book, with the words: Life Lessons That Helped Build QTR, Pike B Dam, And Transform Loviter & BLUZ TV
By Gavin Melrose
The designs I've included here I don't particularly like, although I think you can see my general idea. He is a black and white man, so I have a back and white photo.
A big bold headline and not overly sized black and white

```html
<!DOCTYPE html>
<html lang="en">
<head>
<meta charset="utf-8">
<title>Past the Gravel — Book Cover</title>
<link rel="stylesheet" href="https://fonts.googleapis.com/css2?family=Cinzel:wght@500;600;700&family=Cormorant+Garamond:ital,wght@1,500&display=swap">
<style>
  :root {
    --ink: #050505;
    --paper: #ffffff;
    --gold-deep: #b7832a;
    --gold-mid: #c99232;
    --gold-light: #ecd08a;
    --photo-shadow: #0c0c0c;
    --photo-shirt: #1b1b1b;
    --photo-mid: #4a4743;
    --photo-skin: #8e8a84;
    --photo-highlight: #b3aea6;
  }
  * { margin: 0; padding: 0; box-sizing: border-box; }
  html, body { width: 798px; height: 1200px; overflow: hidden; background: var(--ink); }
  .cover {
    position: relative;
    width: 798px;
    height: 1200px;
    overflow: hidden;
    background: radial-gradient(ellipse at 70% 20%, #171717 0%, var(--ink) 70%);
  }
  .portrait {
    position: absolute;
    left: 140px;
    top: 110px;
    right: 0;
    bottom: 0;
    background:
      radial-gradient(ellipse 165px 215px at 63% 28%, var(--photo-highlight) 0%, var(--photo-skin) 40%, var(--photo-mid) 72%, rgba(74,71,67,0) 100%),
      radial-gradient(ellipse 90px 110px at 58% 52%, rgba(110,106,100,0.85) 0%, rgba(60,58,55,0.5) 60%, rgba(0,0,0,0) 100%),
      radial-gradient(ellipse 340px 90px at 62% 87%, rgba(120,116,110,0.75) 0%, rgba(70,67,63,0.55) 55%, rgba(0,0,0,0) 100%),
      radial-gradient(ellipse 360px 520px at 60% 78%, #262626 0%, var(--photo-shirt) 55%, rgba(12,12,12,0) 100%),
      linear-gradient(90deg, rgba(5,5,5,1) 0%, rgba(18,18,18,0.6) 40%, rgba(28,28,28,0.6) 100%);
  }
  .title-lead {
    position: absolute;
    left: 44px;
    top: 44px;
    font-family: "Cinzel", "Times New Roman", serif;
    font-weight: 700;
    font-size: 78px;
    line-height: 1;
    letter-spacing: 2px;
    color: var(--paper);
    white-space: nowrap;
  }
  .title-main {
    position: absolute;
    left: 142px;
    top: 140px;
    width: 148px;
    height: 688px;
  }
  .subtitle {
    position: absolute;
    left: 58px;
    top: 170px;
    height: 630px;
    writing-mode: vertical-rl;
    text-align: center;
    font-family: "Cormorant Garamond", "Georgia", serif;
    font-style: italic;
    font-weight: 500;
    font-size: 23px;
    line-height: 25px;
    letter-spacing: 1.8px;
    text-transform: uppercase;
    color: var(--paper);
    white-space: nowrap;
  }
  .byline {
    position: absolute;
    left: 90px;
    width: 640px;
    top: 1096px;
    text-align: center;
    font-family: "Cinzel", "Times New Roman", serif;
    font-weight: 600;
    font-size: 44px;
    line-height: 1;
    letter-spacing: 12px;
    white-space: nowrap;
    background: linear-gradient(90deg, var(--gold-deep) 0%, var(--gold-mid) 40%, var(--gold-light) 100%);
    -webkit-background-clip: text;
    background-clip: text;
    color: transparent;
  }
</style>
</head>
<body>
  <main class="cover">
    <div class="portrait" role="img" aria-label="Black and white portrait of the author, arms crossed, wearing a dark polo shirt"></div>

    <h1 class="title-lead">PAST THE</h1>

    <svg class="title-main" viewBox="0 0 148 688" aria-label="GRAVEL">
      <defs>
        <linearGradient id="gold" x1="0" y1="0" x2="688" y2="0" gradientUnits="userSpaceOnUse">
          <stop offset="0" stop-color="#ecd08a"/>
          <stop offset="0.14" stop-color="#b7832a"/>
          <stop offset="0.3" stop-color="#ecd08a"/>
          <stop offset="0.47" stop-color="#b7832a"/>
          <stop offset="0.64" stop-color="#ecd08a"/>
          <stop offset="0.82" stop-color="#b7832a"/>
          <stop offset="1" stop-color="#ecd08a"/>
        </linearGradient>
      </defs>
      <text transform="translate(4,0) rotate(90)" x="0" y="0"
            textLength="688" lengthAdjust="spacingAndGlyphs"
            font-family="Cinzel, 'Times New Roman', serif" font-weight="700" font-size="198"
            fill="url(#gold)">GRAVEL</text>
    </svg>

    <p class="subtitle">Life Lessons That Helped Build QTR,<br>Pike B Dam, And Transform Loviter &amp; BLUZ TV</p>

    <p class="byline">BY GAVIN MELROSE</p>
  </main>
</body>
</html>
```